Web Design Project - Coral Reef Licensing Limited

Coral Reef Licensing Limited is a Vanuatu based License and Compliance Consultant to the Vanuatu Government. We are authorised to review and recommend on all applications for Interactive Gaming Licenses (On Line Casino and Sports/Horse Racing) for the Vanuatu Government.
We need a professional web site that presents us a professional organisation while eye-catching in the same breath.
Examples of some similar operations include:
http://www.northbayloreth.com/html/home.php
http://wagering.qx.example/
http://www.placesopen.example/egaming
We are looking for the final product in code, not PSD please.
Hi all.
We are looking for the project to be a final site, not just PSD please.
Thanks all.
Derek
Target Market(s)
The target market are corporate bookmakers, on line casino and on line poker operators (Interactive Gaming).
in addition we are the first point of contact for anyone looking to Vanuatu as a potential location for licensing.
Industry/Entity Type
Casino
Colors
Designer to choose colors to be used in the design.
Requirements
Must have
- They key things for this site are:
Clear navigation - Needs to be simple and fast to navigate
Visually appealing and simple home page - Speaks for itself
Prominent Contact Information - One of the most important components
FAQ’s - Simple and easy to access such as "who we are, what we do and stored documents"
The site must have the following pages:
Main
Who Are We
Document Repository (12-15 pdf''s)
Reference and links back to the Regulatory Body and relevant pages being:
https://dutiesandlevies.example/index.php/en/inland-revenue/rates-taxes/interactive-gaming-license-tax
and
https://dutiesandlevies.example/index.php/en/inland-revenue/rates-taxes
Contact Us

```html
<!DOCTYPE html>
<html lang="en">
<head>
<meta charset="utf-8">
<title>Gaming Regulator – Coral Reef Licensing Limited</title>
<link rel="stylesheet" href="https://fonts.googleapis.com/css2?family=Open+Sans:wght@300;400;600;700&display=swap">
<style>
:root{
  --blue:#1a4bbf;
  --blue-dark:#0f3a9e;
  --blue-text:#1d47a8;
  --yellow:#e3e81a;
  --grey-bg:#f4f4f4;
  --footer-bg:#e9e9e9;
  --text:#555;
  --dark-tile:#4a4a4a;
  --hero-dark:#12203a;
}
*{box-sizing:border-box;margin:0;padding:0}
html,body{width:758px;height:1200px;overflow:hidden}
body{font-family:"Open Sans",sans-serif;color:var(--text);background:#fff;position:relative;font-size:8px}
a{color:inherit;text-decoration:none}
.abs{position:absolute}

.topbar{left:0;top:0;width:758px;height:23px;background:var(--grey-bg);font-size:6px;color:#888}
.topbar .support{position:absolute;left:65px;top:8px}
.topbar .support b{color:#333;font-weight:400}
.topbar .links{position:absolute;right:65px;top:7px;font-size:7px}

.header{left:0;top:23px;width:758px;height:45px;background:#fff}
.logo{position:absolute;left:65px;top:5px;font-size:17px;font-weight:700;color:var(--blue-text);letter-spacing:1px}
.tagline{position:absolute;left:67px;top:26px;font-size:7px;color:#666}
.search{position:absolute;left:505px;top:11px;width:190px;height:23px;border:1px solid #ddd;background:#fff}
.search span{position:absolute;left:6px;top:6px;font-size:7px;color:#999}
.search .btn{position:absolute;right:-1px;top:-1px;width:24px;height:23px;background:var(--blue)}

.nav{left:0;top:68px;width:758px;height:26px;background:linear-gradient(var(--blue),var(--blue-dark))}
.nav ul{list-style:none;position:absolute;left:65px;top:0;display:flex;height:26px}
.nav li{color:#fff;font-size:8px;font-weight:600;padding:0 13px;line-height:26px;border-right:1px solid rgba(255,255,255,.15)}
.nav li.active{background:#0d3490}
.nav .login{position:absolute;left:628px;top:0;width:67px;height:26px;background:var(--yellow);color:#1a2a60;font-size:7.5px;font-weight:600;text-align:center;line-height:26px}

.hero{left:0;top:94px;width:758px;height:336px;background:radial-gradient(ellipse at 30% 20%,#3a6fb0 0%,#1d3563 45%,var(--hero-dark) 100%)}
.tile{position:absolute}
.t1{left:64px;top:30px;width:188px;height:132px;background:linear-gradient(135deg,#6d89a8,#2c3e55)}
.t2{left:64px;top:164px;width:188px;height:132px;background:linear-gradient(#2e5fcf,#2148a8);color:#fff;text-align:center}
.t2 h3{font-size:11px;font-weight:600;margin-top:34px}
.t2 p{font-size:7px;font-weight:600;line-height:9.5px;padding:4px 18px 0}
.t3{left:255px;top:30px;width:188px;height:266px;background:linear-gradient(170deg,#e8b55c,#8e5a2a 60%,#3c2a1a)}
.t4{left:446px;top:30px;width:249px;height:132px;background:linear-gradient(135deg,#6f7785,#2c3038)}
.t5{left:446px;top:164px;width:123px;height:132px;background:linear-gradient(135deg,#9a9ea6,#3c2a2a)}
.t6{left:572px;top:164px;width:123px;height:132px;background:linear-gradient(135deg,#5f8a74,#28473c)}
.arrow{position:absolute;top:150px;width:22px;height:22px}
.dots{position:absolute;left:364px;top:320px;display:flex;gap:4px}
.dots i{width:5px;height:5px;border-radius:50%;border:1px solid #fff;display:block}
.dots i.on{background:#fff}

.welcome{left:64px;top:461px;width:631px;text-align:center}
.welcome h1{font-size:15px;font-weight:400;color:var(--blue-text)}
.welcome p{font-size:7.4px;font-weight:600;color:#666;line-height:11.2px;margin-top:11px}
.btn-primary{display:inline-block;margin-top:14px;background:var(--blue);color:#fff;font-size:8px;font-weight:600;padding:4px 10px}

.features{left:64px;top:608px;display:flex;gap:12.7px}
.feature{width:116px;height:82px;position:relative;background:linear-gradient(135deg,var(--dark-tile) 50%,#5c5c5c 50%);color:#eee;display:flex;align-items:center;box-shadow:0 6px 6px -3px rgba(0,0,0,.3)}
.feature.active{background:linear-gradient(135deg,#1c4cc4 50%,#2d5fd8 50%);color:#fff}
.feature svg{margin-left:12px;flex:none}
.feature span{flex:1;text-align:center;font-size:9.5px;line-height:15px;padding-right:4px}
.feature.active span{font-weight:600}

.section-title{font-size:15px;font-weight:400;color:var(--blue-text)}
.news{left:64px;top:740px;width:310px}
.news-item{position:absolute;top:42px;width:145px}
.date{position:absolute;left:0;top:0;width:33px;text-align:center}
.date b{font-size:11px;font-weight:700;color:#333;display:block;border-bottom:1px solid var(--blue);padding-bottom:2px}
.date small{font-size:5.5px;letter-spacing:1px;color:#444}
.news-item h4{margin-left:44px;font-size:9px;font-weight:400;color:#333;line-height:15px}
.news-item p{font-size:6.3px;color:#888;line-height:11px;margin-top:14px}
.news-item a{display:block;font-size:6.5px;color:var(--blue-text);margin-top:13px}
.news-nav{position:absolute;left:0;top:152px;display:flex;gap:4px}

.testimonials{left:389px;top:740px;width:307px}
.quote{position:absolute;top:46px;left:2px;width:305px;height:65px;background:#3f454d;color:#ccc;font-size:6.5px;line-height:11px;padding:14px 46px 0 46px}
.quote:after{content:"";position:absolute;left:18px;bottom:-6px;border:6px solid transparent;border-bottom:0;border-top-color:#3f454d}
.author{position:absolute;top:128px;left:2px;font-size:6.5px;color:#333}
.author em{font-style:normal;color:var(--blue-text)}
.tdots{position:absolute;top:153px;left:2px;display:flex;gap:6px}
.tdots i{width:4px;height:4px;border-radius:50%;background:#333;display:block}
.tdots i.on{background:var(--blue)}

.footer{left:0;top:995px;width:758px;height:169px;background:var(--footer-bg)}
.fcol{position:absolute;top:26px}
.fcol h5{font-size:9.5px;font-weight:600;color:#222;margin-bottom:17px}
.fcol ul{list-style:none}
.fcol li{font-size:7.5px;color:#555;line-height:13.3px}
.fcol li:before{content:"›";margin-right:8px}
.addr{font-size:7.5px;color:#555;line-height:12.5px;padding-left:17px;position:relative;margin-bottom:16px}
.addr svg{position:absolute;left:2px;top:2px}
.divider{position:absolute;top:24px;width:1px;height:125px;background:#ddd}
.field{width:101px;height:15px;background:#fff;border:1px solid #ccc;font-size:6.5px;color:#999;padding:3px 5px;margin-bottom:5px}
.field.tall{height:29px}
.send{width:101px;height:18px;background:var(--blue);color:#fff;font-size:7.5px;text-align:center;line-height:18px}
.badge{width:109px;height:33px;margin-bottom:10px}

.bottombar{left:0;top:1164px;width:758px;height:36px;background:var(--blue)}
.bottombar p{position:absolute;left:63px;top:13px;font-size:8px;color:#fff}
.social{position:absolute;left:620px;top:13px;display:flex;gap:10px}
.social i{display:block;width:10px;height:10px;border-radius:50%;background:#fff}
</style>
</head>
<body>

<div class="topbar abs">
  <div class="support">24/7 Support: <b>2 (010)-555-018200</b></div>
  <div class="links">Contact Support &nbsp;/&nbsp; About us &nbsp;/&nbsp; Knowledgebase</div>
</div>

<header class="header abs">
  <div class="logo">Gaming Regulator</div>
  <div class="tagline">Lorem ipsum dolor sit</div>
  <div class="search"><span>Search for</span>
    <div class="btn"><svg width="24" height="23" viewBox="0 0 24 23"><circle cx="13" cy="10" r="4.5" fill="none" stroke="#fff" stroke-width="1.3"/><line x1="9.8" y1="13.3" x2="6.5" y2="16.5" stroke="#fff" stroke-width="1.3"/></svg></div>
  </div>
</header>

<nav class="nav abs">
  <ul>
    <li class="active">Home</li>
    <li>Who are We</li>
    <li>Documents Repository</li>
    <li>References</li>
    <li>Contact us</li>
  </ul>
  <div class="login">Login / Signup</div>
</nav>

<section class="hero abs">
  <div class="tile t1" role="img" aria-label="Photo of a card player holding aces"></div>
  <div class="tile t2">
    <h3>LOREM IPSUM</h3>
    <p>Lorem ipsum dolor sit amet, consectetur adipiscing elit. Suspendisse sed rutrum justo, ac imperdiet</p>
    <svg width="16" height="16" viewBox="0 0 16 16" style="margin-top:6px"><circle cx="8" cy="7" r="6" fill="#fff"/><circle cx="8" cy="7" r="2.5" fill="#2148a8"/><path d="M6 12 L8 15 L10 12Z" fill="#fff"/></svg>
  </div>
  <div class="tile t3" role="img" aria-label="Photo of a cyclist carrying a bike up steps at sunset"></div>
  <div class="tile t4" role="img" aria-label="Photo of a stock exchange building with a flag"></div>
  <div class="tile t5" role="img" aria-label="Photo of a wrestling match with a referee"></div>
  <div class="tile t6" role="img" aria-label="Photo of a tennis player hitting a ball"></div>
  <svg class="arrow" style="left:17px" viewBox="0 0 22 22"><circle cx="11" cy="11" r="10" fill="none" stroke="#cfd8e8" stroke-width="1.4"/><path d="M15 11H7M10 7.5 6.5 11 10 14.5" fill="none" stroke="#cfd8e8" stroke-width="1.4"/></svg>
  <svg class="arrow" style="left:714px" viewBox="0 0 22 22"><circle cx="11" cy="11" r="10" fill="none" stroke="#cfd8e8" stroke-width="1.4"/><path d="M7 11H15M12 7.5 15.5 11 12 14.5" fill="none" stroke="#cfd8e8" stroke-width="1.4"/></svg>
  <div class="dots"><i class="on"></i><i></i><i></i></div>
</section>

<section class="welcome abs">
  <h1>WELCOME TO OUR SITE</h1>
  <p>Are you ready for something refreshingly different? Would you like to be able to talk with someone who understands your business challenges and can deliver customized services and solutions that truly add value to your organization?&nbsp; Are you looking for someone to provide expertise at reasonable rates?We are Reefline Services. We listen to you so we can speak your language and work within your means to elegantly solve the information technology challenges that are specific to your company.</p>
  <a class="btn-primary">Read More</a>
</section>

<section class="features abs">
  <div class="feature active">
    <svg width="30" height="34" viewBox="0 0 30 34"><circle cx="15" cy="13" r="10" fill="none" stroke="#fff" stroke-width="2"/><ellipse cx="15" cy="13" rx="4.5" ry="10" fill="none" stroke="#fff" stroke-width="1.6"/><line x1="5" y1="13" x2="25" y2="13" stroke="#fff" stroke-width="1.6"/><path d="M2 20 Q6 31 15 31 Q24 31 28 20" fill="none" stroke="#fff" stroke-width="3"/></svg>
    <span>Statues<br>&amp;<br>Regulation</span>
  </div>
  <div class="feature">
    <svg width="24" height="28" viewBox="0 0 24 28"><path d="M1 1H16L23 8V27H1Z" fill="#fff"/><g stroke="#4a4a4a" stroke-width="1.8"><line x1="5" y1="11" x2="19" y2="11"/><line x1="5" y1="16" x2="19" y2="16"/><line x1="5" y1="21" x2="19" y2="21"/></g></svg>
    <span>Licence<br>Information</span>
  </div>
  <div class="feature">
    <svg width="28" height="20" viewBox="0 0 28 20"><path d="M6 2H22Q27 2 27.5 10L27 17Q25 20 22 16L19 13H9L6 16Q3 20 1 17L0.5 10Q1 2 6 2Z" fill="#fff"/><g fill="#4a4a4a"><rect x="5" y="7.5" width="6" height="2"/><rect x="7" y="5.5" width="2" height="6"/><circle cx="20" cy="7" r="1.3"/><circle cx="22.5" cy="9.5" r="1.3"/></g></svg>
    <span>Interactive<br>Gaming<br>Licenses</span>
  </div>
  <div class="feature">
    <svg width="18" height="24" viewBox="0 0 18 24"><rect x="1" y="1" width="16" height="22" fill="none" stroke="#fff" stroke-width="1.5"/><g stroke="#fff" stroke-width="1.2"><rect x="4" y="5" width="3" height="3" fill="none"/><line x1="9" y1="6.5" x2="14" y2="6.5"/><rect x="4" y="10.5" width="3" height="3" fill="none"/><line x1="9" y1="12" x2="14" y2="12"/><rect x="4" y="16" width="3" height="3" fill="none"/><line x1="9" y1="17.5" x2="14" y2="17.5"/></g></svg>
    <span>Review<br>and<br>Recommend</span>
  </div>
  <div class="feature">
    <svg width="26" height="20" viewBox="0 0 26 20"><rect x="1" y="1" width="24" height="18" fill="#fff"/><rect x="4" y="5" width="7" height="6" fill="#4a4a4a"/><g stroke="#4a4a4a" stroke-width="1.3"><line x1="13" y1="6" x2="22" y2="6"/><line x1="13" y1="10" x2="22" y2="10"/><line x1="4" y1="14.5" x2="22" y2="14.5"/></g></svg>
    <span>Tax<br>Forms</span>
  </div>
</section>

<section class="news abs">
  <h2 class="section-title">LATEST NEWS</h2>
  <article class="news-item" style="left:0">
    <div class="date"><b>03</b><small>DEC. 13</small></div>
    <h4>Cum Sociis Natoque Penatibus Et Magnis...</h4>
    <p>Suspendisse pulvinar felis eu consequat mattis. Proin euismod placerat consectetur. Proin dapibus ante id eros...</p>
    <a>Read More...</a>
  </article>
  <article class="news-item" style="left:163px">
    <div class="date"><b>11</b><small>DEC. 13</small></div>
    <h4>Duis Molestie Mi Non Ante Condimentum...</h4>
    <p>Praesent nibh leo, sagittis vel risus iaculis, sagittis ullamcorper ligula. In ultrices mi eget dolor dapibus, sed...</p>
    <a>Read More...</a>
  </article>
  <div class="news-nav">
    <svg width="14" height="14" viewBox="0 0 14 14"><circle cx="7" cy="7" r="6" fill="none" stroke="#777"/><path d="M10 7H4M6.5 4.5 4 7 6.5 9.5" fill="none" stroke="#777"/></svg>
    <svg width="14" height="14" viewBox="0 0 14 14"><circle cx="7" cy="7" r="6" fill="none" stroke="#1d47a8" stroke-width="1.2"/><path d="M4 7H10M7.5 4.5 10 7 7.5 9.5" fill="none" stroke="#1d47a8" stroke-width="1.2"/></svg>
  </div>
</section>

<section class="testimonials abs">
  <h2 class="section-title">TESTIMONIALS</h2>
  <blockquote class="quote">
    <svg class="abs" style="left:16px;top:14px" width="12" height="9" viewBox="0 0 12 9"><path d="M0 9V5Q0 0 5 0V2Q2 2 2 4H5V9ZM7 9V5Q7 0 12 0V2Q9 2 9 4H12V9Z" fill="#2d6be0"/></svg>
    Etiam in tincidunt arcu, at tempor magna. Maecenas ut odio nunc. Fusce aliquet sem et sollicitudin tincidunt. Aliquam convallis vitae metus ut luctus....
    <svg class="abs" style="right:14px;top:40px" width="12" height="9" viewBox="0 0 12 9"><path d="M12 0V4Q12 9 7 9V7Q10 7 10 5H7V0ZM5 0V4Q5 9 0 9V7Q3 7 3 5H0V0Z" fill="#2d6be0"/></svg>
  </blockquote>
  <div class="author">John Doe, <em>developer</em></div>
  <div class="tdots"><i class="on"></i><i></i><i></i></div>
</section>

<footer class="footer abs">
  <div class="fcol" style="left:63px">
    <h5>LINKS</h5>
    <ul><li>Home</li><li>Who are We</li><li>Documents Repository</li><li>References</li><li>Contact us</li></ul>
  </div>
  <div class="divider" style="left:180px"></div>
  <div class="fcol" style="left:236px">
    <h5>LOCATION</h5>
    <div class="addr"><svg width="7" height="9" viewBox="0 0 7 9"><path d="M3.5 9 0.5 4A3 3 0 1 1 6.5 4Z" fill="#aaa"/></svg>Harbourview, 22 southwest<br>48 Palm Terrace<br>Port Lena, VT 04410</div>
    <div class="addr"><svg width="7" height="9" viewBox="0 0 7 9"><path d="M3.5 9 0.5 4A3 3 0 1 1 6.5 4Z" fill="#aaa"/></svg>Mele Bay, 7/12 northeast<br>48 Palm Terrace<br>Port Lena, VT 04410</div>
  </div>
  <div class="divider" style="left:386px"></div>
  <div class="fcol" style="left:419px">
    <h5>CONTACT US</h5>
    <div class="field">Name</div>
    <div class="field">Email</div>
    <div class="field tall">Message</div>
    <div class="send">Contact</div>
  </div>
  <div class="divider" style="left:552px"></div>
  <div class="fcol" style="left:582px">
    <h5>CUSTOMS</h5>
    <div class="badge" style="background:#1f5a2a;border:2px solid #cfd8cf" role="img" aria-label="Partner authority badge"></div>
    <div class="badge" style="background:#7a1a20;border:2px solid #d8cfcf" role="img" aria-label="Partner corporation badge"></div>
  </div>
</footer>

<div class="bottombar abs">
  <p>Copyright © yourwebsite &nbsp;| &nbsp;Terms &amp; Conditions</p>
  <div class="social"><i></i><i></i><i></i><i></i></div>
</div>

</body>
</html>
```